Premium Gold Vodka Label Design

English ------------------- We need a label for a Vodka Bottle. Its a sparkling premium vodka with gold inside. The design should look premium. We tried it on our selves but it looks horrible. Therefore we need your help. The current name is lumora K, but we are open for any better suggestion. We attached the selfmade design. The label will be printed on the bottle. We have other design jobs for you (logo, other sorts)! English ------------------------ We need a label for a vodka bottle. This is a premium vodka which is offset with gold. The design should look like this. We have tried so far and failed. That is why we need your support. The name is so far lumora K. If you have better suggestions we would be pleased about other suggestions / ideas. In the appendix the failed design is stored. The label is to be applied by screen printing. In the case of good work follow-up projects are guaranteed (logo, other varieties, etc)!
Updates

Project Deadline Extended
Reason: We need more time for the decision.

Target Market(s)

USA

Colors

Designer to choose colors to be used in the design.

Requirements
Must have
• English ------------------------ The needed text is on our selfmade label that is attached. English ------------------------ The required texts are stored in the attached design.
Nice to have
• English ------------------------ Transparent places are allowed because we want to print the label on the bottom. English ------------------------ As the label is applied by screen printing, transparent areas are also possible.

```html
<!DOCTYPE html>
<html lang="en">
<head>
<meta charset="utf-8">
<title>Lumora — 24 KT Premium Gold Sparkling Vodka Label</title>
<link rel="stylesheet" href="https://fonts.googleapis.com/css2?family=Montserrat:wght@700&family=Oswald:wght@300;400;500&display=swap">
<style>
  :root {
    --page: #ffffff;
    --wine-dark: #3a0604;
    --wine: #6e0d06;
    --wine-bright: #8c1208;
    --gold-light: #fff2a8;
    --gold: #e0b52c;
    --gold-deep: #a97a10;
    --cream: #f6f6ea;
    --cream-shade: #d9dccb;
    --ink: #2b1d12;
    --star-dark: #111111;
  }
  html, body {
    margin: 0;
    padding: 0;
    width: 696px;
    height: 1200px;
    overflow: hidden;
    background: var(--page);
  }
  .label {
    display: block;
    width: 696px;
    height: 1200px;
  }
  .brand-name {
    font-family: "Montserrat", sans-serif;
    font-weight: 700;
    font-size: 40px;
    fill: var(--gold);
  }
  .karat {
    font-family: "Oswald", sans-serif;
    font-weight: 500;
    font-size: 33px;
    fill: var(--ink);
  }
  .subtitle {
    font-family: "Oswald", sans-serif;
    font-weight: 300;
    font-size: 19px;
    fill: var(--ink);
  }
  .product {
    font-family: "Oswald", sans-serif;
    font-weight: 500;
    font-size: 86px;
  }
  .details {
    font-family: "Oswald", sans-serif;
    font-weight: 300;
    font-size: 22px;
    fill: var(--gold);
  }
  .details .emphasis { font-weight: 500; }
  .specs {
    font-family: "Oswald", sans-serif;
    font-weight: 400;
    font-size: 15px;
    fill: var(--ink);
  }
</style>
</head>
<body>
<svg class="label" viewBox="0 0 484 834" preserveAspectRatio="xMidYMid meet" xmlns="http://www.w3.org/2000/svg">
  <defs>
    <linearGradient id="wine-sheen" x1="0" y1="0" x2="1" y2="0">
      <stop offset="0" stop-color="var(--wine)"/>
      <stop offset="0.3" stop-color="var(--wine-dark)"/>
      <stop offset="0.55" stop-color="var(--wine-bright)"/>
      <stop offset="0.8" stop-color="var(--wine-dark)"/>
      <stop offset="1" stop-color="var(--wine)"/>
    </linearGradient>
    <linearGradient id="gold-frame" x1="0" y1="0" x2="1" y2="1">
      <stop offset="0" stop-color="var(--gold-deep)"/>
      <stop offset="0.35" stop-color="var(--gold-light)"/>
      <stop offset="0.6" stop-color="var(--gold)"/>
      <stop offset="1" stop-color="var(--gold-deep)"/>
    </linearGradient>
    <linearGradient id="gold-type" x1="0" y1="0" x2="1" y2="0">
      <stop offset="0" stop-color="var(--gold-deep)"/>
      <stop offset="0.45" stop-color="var(--gold-light)"/>
      <stop offset="1" stop-color="var(--gold)"/>
    </linearGradient>
    <linearGradient id="cream-band" x1="0" y1="0" x2="1" y2="0">
      <stop offset="0" stop-color="var(--cream-shade)"/>
      <stop offset="0.5" stop-color="var(--cream)"/>
      <stop offset="1" stop-color="var(--cream-shade)"/>
    </linearGradient>
    <path id="label-outline" d="M110,48 Q242,4 374,48 L374,70 Q380,92 410,92 L410,110 Q432,110 432,132 L432,700 Q432,722 410,722 L410,742 Q380,742 374,764 L374,786 Q242,830 110,786 L110,764 Q104,742 74,742 L74,722 Q52,722 52,700 L52,132 Q52,110 74,110 L74,92 Q104,92 110,70 Z"/>
    <clipPath id="label-clip"><use href="#label-outline"/></clipPath>
    <path id="star" d="M0,-7 L2,-2.2 7,-2.2 3,0.9 4.5,6 0,3 -4.5,6 -3,0.9 -7,-2.2 -2,-2.2 Z"/>
  </defs>

  <!-- label body -->
  <g class="label-body">
    <use href="#label-outline" fill="url(#wine-sheen)" stroke="url(#gold-frame)" stroke-width="12"/>
    <g clip-path="url(#label-clip)">
      <rect class="band-top" x="40" y="196" width="404" height="104" fill="url(#cream-band)"/>
      <rect class="band-bottom" x="40" y="618" width="404" height="220" fill="url(#cream-band)"/>
    </g>
    <use href="#label-outline" fill="none" stroke="url(#gold-frame)" stroke-width="2"
         transform="translate(242 417) scale(0.955 0.972) translate(-242 -417)"/>
  </g>

  <!-- stars -->
  <g class="stars-top" fill="url(#gold-frame)">
    <use href="#star" x="182" y="44"/>
    <use href="#star" x="212" y="38"/>
    <use href="#star" x="242" y="36"/>
    <use href="#star" x="272" y="38"/>
    <use href="#star" x="302" y="44"/>
  </g>
  <g class="stars-bottom" fill="var(--star-dark)">
    <use href="#star" x="182" y="762"/>
    <use href="#star" x="212" y="770"/>
    <use href="#star" x="242" y="774"/>
    <use href="#star" x="272" y="770"/>
    <use href="#star" x="302" y="762"/>
  </g>

  <!-- text -->
  <text class="brand-name" x="242" y="162" text-anchor="middle">Lumora</text>
  <text class="karat" x="242" y="240" text-anchor="middle">24 KT</text>
  <text class="subtitle" x="242" y="272" text-anchor="middle">PREMIUM GOLD&#160;&#160;SPARKLING</text>
  <text class="product" x="242" y="462" text-anchor="middle" fill="url(#gold-type)">VODKA</text>
  <text class="details" x="242" y="518" text-anchor="middle">DISTILLED <tspan class="emphasis">8</tspan> FILTERED</text>
  <text class="details" x="242" y="558" text-anchor="middle">MADE IN GERMANY</text>
  <text class="specs" x="242" y="704" text-anchor="middle">40% ALC VOL&#160;&#160;|&#160;&#160;200 ML&#160;&#160;|&#160;&#160;80 PROOF</text>
</svg>
</body>
</html>
```